Letterhead Design Project

We have recently updated our corporate logo and are seeking a new letterhead template.

Attached is the new logo and the old letterhead.

PLEASE DO NOT USE OUR EXISTING WEB SITE FOR INSPIRATION as we are redesigning it.

Target Market(s)

Executives, search professionals, technical and scientific professionals

Industry/Entity Type

Seeking

```html
<!DOCTYPE html>
<html lang="en">
<head>
<meta charset="utf-8">
<title>HelixSeek Letterhead</title>
<link rel="stylesheet" href="https://fonts.googleapis.com/css2?family=Arimo:wght@400;700&family=Montserrat:wght@700&display=swap">
<style>
  :root {
    --brand-blue: #2b9fd8;
    --text-grey: #6b6f72;
    --tint-blue: #e7f2f9;
    --paper: #ffffff;
  }
  html, body {
    margin: 0;
    padding: 0;
    width: 848px;
    height: 1200px;
    overflow: hidden;
    background: var(--paper);
  }
  .letterhead {
    position: relative;
    width: 848px;
    height: 1200px;
    overflow: hidden;
    background: var(--paper);
  }
  .backdrop-disc {
    position: absolute;
    left: 0;
    top: 0;
    width: 848px;
    height: 1200px;
  }
  .brand {
    position: absolute;
    left: 62px;
    top: 56px;
    display: flex;
    align-items: center;
    gap: 10px;
  }
  .brand-dot {
    width: 46px;
    height: 46px;
    border-radius: 50%;
    background: var(--brand-blue);
  }
  .brand-name {
    font-family: "Montserrat", Arial, sans-serif;
    font-weight: 700;
    font-size: 37px;
    letter-spacing: -0.5px;
    color: var(--brand-blue);
    line-height: 1;
  }
  .contact-line {
    position: absolute;
    left: 774px;
    top: 1135px;
    transform-origin: left top;
    transform: rotate(-90deg);
    white-space: nowrap;
    font-family: "Arimo", Helvetica, Arial, sans-serif;
    font-size: 13.4px;
    line-height: 16px;
    color: var(--text-grey);
  }
  .contact-web {
    color: var(--brand-blue);
    font-weight: 700;
    margin-left: 6px;
  }
</style>
</head>
<body>
  <main class="letterhead">
    <svg class="backdrop-disc" viewBox="0 0 848 1200" aria-hidden="true">
      <circle cx="732" cy="936" r="288" fill="var(--tint-blue)"/>
    </svg>

    <header class="brand">
      <span class="brand-dot"></span>
      <span class="brand-name">HelixSeek</span>
    </header>

    <address class="contact-line">
      voice 555.210.0140, fax 555.210.0140, 240 Harbor Field Road, Suite 310, Millbrook, MA 01999,
      <span class="contact-web">www.helixseek.com</span>
    </address>
  </main>
</body>
</html>
```